Business card - Brio Margin - size 85 mm * 55 mm

We need new business cards. Design must fit with our vision of the firm. You find in the attached file our logo and a short description of our firm (mission, vision, value, business and so on).

Target Market(s)

Consulting firm in performance improvement

Industry/Entity Type

Management Consulting

Contact Information for Business Card

SIZE
85 mm * 55 mm
INFORMATIONS
name surname
role position
telephone number
email address

Requirements
Must have
• the brand must APPEAR for the rest Would we like to have something sleek, inspired to a "just right" approach
Should not have
• Please avoid the black color as background

```html
<!DOCTYPE html>
<html lang="en">
<head>
<meta charset="utf-8">
<title>Brio Margin – Business Card</title>
<link rel="stylesheet" href="https://fonts.googleapis.com/css2?family=Open+Sans:wght@400;600&display=swap">
<style>
  :root {
    --orange: #e8781e;
    --orange-deep: #d2621a;
    --orange-light: #ef9a35;
    --charcoal: #252a2e;
    --ink: #1e1e1e;
    --grey: #555;
    --paper: #ffffff;
    --paper-shade: #eeeeee;
    --stage: #e9e6e2;
  }
  * { box-sizing: border-box; margin: 0; padding: 0; }
  html, body { width: 1200px; height: 1023px; overflow: hidden; }
  body {
    background: var(--stage);
    font-family: "Open Sans", Arial, sans-serif;
    position: relative;
  }
  .card {
    position: absolute;
    width: 540px;
    height: 349px;
    border-radius: 18px;
    overflow: hidden;
    box-shadow: 0 6px 18px rgba(0,0,0,.18);
  }
  /* Front */
  .card-front {
    left: 40px; top: 337px;
    background: linear-gradient(135deg, var(--paper) 0%, var(--paper) 60%, var(--paper-shade) 100%);
  }
  .front-band {
    position: absolute; left: 0; bottom: 0; height: 30px; width: 100%;
    display: flex;
  }
  .front-band .band-orange { flex: 0 0 80%; background: linear-gradient(90deg, var(--orange-deep), var(--orange-light)); }
  .front-band .band-gap { flex: 0 0 1.5%; background: var(--paper); }
  .front-band .band-dark { flex: 1; background: var(--charcoal); }

  .brand-block {
    position: absolute; left: 20px; top: 40px; width: 236px; height: 160px;
    display: flex; align-items: center; justify-content: center;
  }
  .brand-name {
    color: var(--orange);
    font-size: 20px; font-weight: 400;
    letter-spacing: 7px;
    white-space: nowrap;
  }
  .divider {
    position: absolute; left: 268px; top: 40px; width: 1px; height: 150px;
    background: var(--orange);
  }
  .contact {
    position: absolute; left: 290px; top: 36px;
  }
  .person-name { font-size: 19px; color: var(--orange); font-weight: 400; }
  .person-name strong { font-weight: 600; }
  .person-role { font-size: 11px; color: var(--grey); }
  .contact-list { list-style: none; margin-top: 22px; }
  .contact-list li {
    display: flex; align-items: center; gap: 10px;
    font-size: 14px; color: var(--ink); margin-bottom: 10px;
  }
  .contact-list svg { width: 15px; height: 15px; flex: none; }

  /* Back */
  .card-back {
    left: 620px; top: 337px;
    background: radial-gradient(circle at 55% 45%, var(--orange-light) 0%, var(--orange) 55%, var(--orange-deep) 100%);
    display: flex; align-items: center; justify-content: center;
  }
  .card-back .brand-name { color: var(--paper); font-size: 24px; letter-spacing: 9px; }
</style>
</head>
<body>
  <section class="card card-front" aria-label="Business card front">
    <div class="brand-block">
      <div class="brand-name">BRIO MARGIN</div>
    </div>
    <div class="divider"></div>
    <div class="contact">
      <p class="person-name"><strong>Your</strong> Name</p>
      <p class="person-role">Position</p>
      <ul class="contact-list">
        <li>
          <svg viewBox="0 0 16 16"><circle cx="8" cy="8" r="7" fill="none" stroke="#e8781e" stroke-width="1.4"/><path d="M5.5 5c0 3 2.5 5.5 5.5 5.5l.5-1.5-1.6-.8-.8.8c-1-.5-1.6-1.2-2-2l.8-.8L7 4.5z" fill="#e8781e"/></svg>
          (88) 555 01234
        </li>
        <li>
          <svg viewBox="0 0 16 16"><rect x="1" y="3.5" width="14" height="9" fill="#e8781e"/><path d="M1 3.5l7 5 7-5" fill="none" stroke="#fff" stroke-width="1.2"/></svg>
          info@briomargin.com
        </li>
        <li>
          <svg viewBox="0 0 16 16" fill="none" stroke="#e8781e" stroke-width="1.2"><circle cx="8" cy="8" r="6.5"/><ellipse cx="8" cy="8" rx="3" ry="6.5"/><path d="M1.5 8h13M2.5 5h11M2.5 11h11"/></svg>
          www.briomargin.com
        </li>
      </ul>
    </div>
    <div class="front-band">
      <div class="band-orange"></div>
      <div class="band-gap"></div>
      <div class="band-dark"></div>
    </div>
  </section>

  <section class="card card-back" aria-label="Business card back">
    <div class="brand-name">BRIO MARGIN</div>
  </section>
</body>
</html>
```